Moderne CI für einen Immobilienmakler [www.hefner-wohnwerte.de]
Zielgruppe
Kunden für hochwertige Immobilien, also gemischtes eher anspruchvolles Klientel.
Hallo,
ich betreibe ein junges Immobilienunternehmen im 4. Geschäftsjahr. Wir vermarkten ausschließlich hochwertige Immobilien. Meine derzeitiges Logo habe ich damals selbst entworfen und es harmoniert gut mit meiner Website [www.hefner-wohnwerte.de] leider habe ich für Printmedien nie eine CI hinbekommen die mir richtig gefällt und die im Gesamt- und Farbkonzept zu meinem Onlineauftritt passt.
Ich wünsche mir nun von einem professionellen Designer eine modern- edle CI mit Entwürfen für Briefpapier, Umschläge C4 und DL, A4 Exposé-Mappe sowie die Rohlinge für eine Dreiseiter Image-Broschüre, für ein Objekt Expose sowie für eine Print-Annonce.
Eine spätere Zusammenarbeit für weitere Medien ist erwünscht.

```html
<!DOCTYPE html>
<html lang="de">
<head>
<meta charset="utf-8">
<title>Hefner Wohnwerte – Geschäftsausstattung</title>
<link rel="stylesheet" href="https://fonts.googleapis.com/css2?family=Arimo:wght@400;700&display=swap">
<style>
  :root {
    --brand-red: #e2001a;
    --ink: #222222;
    --ink-soft: #444444;
    --grey: #8a8a8a;
    --grey-light: #b5b5b5;
    --paper: #ffffff;
    --paper-shade: #cfcfcf;
    --backdrop: #ecebe8;
  }
  * { box-sizing: border-box; margin: 0; padding: 0; }
  html, body { width: 1200px; height: 1200px; overflow: hidden; }
  body {
    background: var(--backdrop);
    font-family: "Arimo", Arial, sans-serif;
    color: var(--ink);
    position: relative;
  }

  /* ---------- Letterhead ---------- */
  .letterhead {
    position: absolute; left: 37px; top: 37px;
    width: 795px; height: 1125px;
    background: linear-gradient(180deg, var(--paper) 0%, var(--paper) 62%, var(--paper-shade) 100%);
    box-shadow: 0 2px 10px rgba(0,0,0,.15);
    overflow: hidden;
  }
  .wordmark {
    position: absolute; color: var(--grey);
    font-weight: 400; letter-spacing: -0.5px; white-space: nowrap;
  }
  .letterhead .wordmark { right: 82px; top: 48px; font-size: 30px; }

  .sender-line { position: absolute; left: 94px; top: 172px; font-size: 9.5px; color: var(--grey); }
  .sender-line .dot { color: var(--brand-red); }
  .recipient { position: absolute; left: 94px; top: 186px; font-size: 15.5px; line-height: 21px; color: var(--ink); font-style: normal; }
  .recipient strong { font-weight: 700; }

  .contact { position: absolute; left: 594px; top: 170px; font-size: 10px; line-height: 13px; color: var(--ink-soft); }
  .contact .name { font-size: 12.5px; line-height: 15px; color: var(--ink); }
  .contact .firm { color: var(--grey-light); font-size: 9.5px; }
  .contact .firm .bar, .footer .bar { color: var(--brand-red); }
  .contact .block { margin-top: 13px; }
  .contact dl { display: grid; grid-template-columns: 0 auto; column-gap: 10px; }
  .contact dt { text-align: right; justify-self: end; white-space: nowrap; }
  .contact dd { white-space: nowrap; }

  .date { position: absolute; right: 75px; top: 349px; font-size: 13px; color: var(--ink-soft); }
  .fold-mark { position: absolute; left: 0; top: 372px; width: 30px; height: 1px; background: var(--grey-light); }
  .punch-mark { position: absolute; left: 0; top: 554px; width: 0; height: 0;
    border-top: 8px solid transparent; border-bottom: 8px solid transparent; border-left: 8px solid var(--brand-red); }

  .subject { position: absolute; left: 94px; top: 389px; font-size: 19px; font-weight: 400; color: var(--grey); white-space: nowrap; }
  .subject .divider { color: var(--brand-red); margin: 0 4px; }
  .subject .topic { color: var(--ink-soft); }

  .letter-body { position: absolute; left: 94px; top: 440px; width: 630px; font-size: 12.8px; line-height: 19.6px; color: var(--ink-soft); }
  .letter-body .salutation { font-size: 15px; font-weight: 700; color: var(--ink); line-height: 20px; }
  .letter-body p + p { margin-top: 9px; }
  .letter-body h3 { font-size: 14px; font-weight: 700; color: var(--ink); margin-top: 20px; line-height: 18px; }
  .bullets { list-style: none; display: grid; grid-template-columns: 213px 213px 204px; margin-top: 2px; }
  .bullets li { line-height: 20px; font-size: 12.4px; }
  .bullets li::before { content: "•"; color: var(--brand-red); margin-right: 4px; }
  .letter-body .closing { margin-top: 18px; }

  .footer { position: absolute; left: 94px; top: 1055px; display: flex; font-size: 9.5px; line-height: 14px; color: var(--ink-soft); }
  .footer .firm-name { font-weight: 700; }
  .footer .rule { width: 2px; height: 46px; background: var(--brand-red); margin: 0 54px 0 52px; }

  /* ---------- Business cards ---------- */
  .card { position: absolute; width: 360px; height: 232px; overflow: hidden; box-shadow: 0 2px 10px rgba(0,0,0,.15); }
  .card-front { left: 802px; top: 543px; background: linear-gradient(180deg, var(--paper) 0%, var(--paper) 55%, var(--paper-shade) 100%); }
  .card-back { left: 802px; top: 813px; background: var(--brand-red); }
  .card-front .wordmark { right: 22px; top: 24px; font-size: 18.5px; }
  .card-person { position: absolute; left: 25px; top: 91px; }
  .card-person .name { font-size: 15px; font-weight: 700; color: var(--ink-soft); }
  .card-person .role { font-size: 11px; color: var(--grey-light); margin-top: 1px; }
  .card-contact { position: absolute; left: 120px; top: 94px; font-size: 11px; line-height: 15px; color: var(--ink-soft); }
  .card-contact dl { display: grid; grid-template-columns: 68px auto; column-gap: 13px; }
  .card-contact dt { text-align: right; }
  .card-contact .gap { margin-top: 8px; }
</style>
</head>
<body>

<article class="letterhead" aria-label="Briefbogen">
  <div class="wordmark">hefner wohnwerte</div>

  <p class="sender-line">Hefner Wohnwerte <span class="dot">•</span> Lindenhof 14 <span class="dot">•</span> D-35039 Marburg</p>
  <address class="recipient">
    <strong>Herr Beispielmann</strong><br>
    Firma Nordstern GmbH &amp; Co. KG<br>
    z.H. Frau Lena Kramer<br>
    Ulmenweg 9–11<br>
    D-10715 Berlin
  </address>

  <div class="contact">
    <div class="name">Jonas Hefner</div>
    <div class="firm">Hefner <span class="bar">|</span> Wohnwerte</div>
    <div class="block">Lindenhof 14<br>D - 35039 Marburg</div>
    <dl class="block"><dt>tel.:</dt><dd>+49 (0)6421 5550183</dd><dt>fax:</dt><dd>+49 (0)6421 5550185</dd></dl>
    <dl class="block"><dt>e-mail:</dt><dd>info@hefner-wohnwerte.de</dd><dt>web:</dt><dd>www.hefner-wohnwerte.de</dd></dl>
  </div>

  <p class="date">16. September 2009</p>
  <span class="fold-mark"></span>
  <span class="punch-mark"></span>

  <h2 class="subject">Marburg-Kernstadt <span class="divider">|</span> <span class="topic">Neubau Architektenhäuser</span></h2>

  <div class="letter-body">
    <p class="salutation">Sehr geehrte Damen und Herren.</p>
    <p>Faccumsandip eriure vel iustin elendrem etum illa feuguer adigna feu feugait lore dolum in et, con ulla-or incilla feuis aut etue tin henit la alis eui tis accum dit veliqua tionsequat lortie feu feuguerat. Em dunt venisl init ut iriuscidiusl doloreet, quat, quat.</p>
    <p>Lutat ulput il essequa mcommol orerciduis ex exero cons aliquis molent vel irilluptat lum dolore conullu ptatinim ipis alit iurem non enis dio od euipis nit alit prate minci bla consed magna feugue veril ut pratin utat augue erostislit ad magniat uerciduis nonsecte del ut praesto od dolobor tionullut loreetue facipsum quisi blaore facip ex exercil iquipsum ing nt autat. Ut illuptat, doluptate magnim dunt at am adiamet vel ex esectet incipsu scipsum dolore del deliquipit dolesse dolobore moloreet alis et in ercidunt inismod oloborem irit il il do consequat, quamcon sequat, si dolesectem nonsecte velit ametuer cipsustrud te enit luptate magnim volortio eugiat ilit praesse tem nit augue volor sed modit et wisi.</p>
    <h3>Überschrift 02</h3>
    <ul class="bullets">
      <li>Aufzählungspunkt</li><li>Aufzählungspunkt</li><li>Aufzählungspunkt</li>
      <li>Aufzählungspunkt</li><li>Aufzählungspunkt</li><li>Aufzählungspunkt</li>
      <li>Aufzählungspunkt</li><li>Aufzählungspunkt</li><li>Aufzählungspunkt</li>
      <li>Aufzählungspunkt</li><li>Aufzählungspunkt</li><li>Aufzählungspunkt</li>
    </ul>
    <p class="closing">Od dip eu feugait acidunt incidunt ullan henismolore mincilisim iriure ex el eu faccum velitCinim iusciniam quatueraesed magna feum vel et el doloreetue conulpute magnim iuscillum iriusto odolor sequat. Bo-rezzrilis molore feum eraestrud vullam nonsequat nulla con utpatet nostis num aliquis el iustrud dolutat. Incipit lum doloreaese modolorpero nis nulputat. Ilisi blam dolore mod magnisim nulput pratummy num eraessi eraesent iniam, quat nim dip elessim deliqui sciliquisi endiatue dit nos non henit. Et amet ad tatie te tatummy nim nos eugait am eugiam ilisi ex eui blam diam, quis nonsequisisi blam estismo dolobor erae stincing ex esto dolum quatum velit in utem verit ipit inlit, sendit utat. Duis aute feugue magna ad tie con essed exeros aliquatue dolobore molestion verit ipit, quis et ate feum quate dolobore tat exeriure tin vel dipsum velessi.</p>
  </div>

  <footer class="footer">
    <div><span class="firm-name">Hefner <span class="bar">|</span> Wohnwerte</span><br>Lindenhof 14<br>D - 35039 Marburg</div>
    <span class="rule"></span>
    <div>Immobilienmakler gem. §34c GewO<br>Steuernummer: 03199200417 Finanzamt Marburg<br>Verantwortlicher gemäss § 6 MDStV: Jonas Hefner</div>
  </footer>
</article>

<section class="card card-front" aria-label="Visitenkarte Vorderseite">
  <div class="wordmark">hefner wohnwerte</div>
  <div class="card-person">
    <div class="name">Jonas Hefner</div>
    <div class="role">Immobilienmakler</div>
  </div>
  <div class="card-contact">
    <dl><dt></dt><dd>Lindenhof 14</dd><dt></dt><dd>D - 35039 Marburg</dd></dl>
    <dl class="gap"><dt>tel.:</dt><dd>+49 (0)6421 5550183</dd><dt>fax:</dt><dd>+49 (0)6421 5550185</dd></dl>
    <dl class="gap"><dt>e-mail:</dt><dd>info@hefner-wohnwerte.de</dd><dt>web:</dt><dd>www.hefner-wohnwerte.de</dd></dl>
  </div>
</section>

<section class="card card-back" aria-label="Visitenkarte Rückseite"></section>

</body>
</html>
```